ebook front & back cover design: 'The Copper Lantern'

I am independent author writing under the pseudonym Reiko Matsudaira. I have already one novel published. I have written another historical novel, set in Japan in the 1950s. It is called 'The Copper Lantern'. The sub-title is 'A female spy uncovers secret weapons testing in cold-war Japan.' Japan in the 1950s was rocked by labour unrest and fear the Korean war would expand. The country was still governed by the US. The back cover copy is 'The Korean war has exploded. Neighbouring Japan is the staging post for US troops. Moscow encourages sabotage with its newly expanded spy network. There is a scramble to develop new weapons. Tungsten, a key component for shells, is scarce.

A communist sympathiser turned provocateur uncovers a secret weapons testing facility. The leaked news petrifies Washington and Tokyo. A talented counter intelligence officer is charged with tracking down the Soviet intelligence network. Is it too late?'

I want a design that communicates intrigue in the context of plot. The font for the author should be consistent with the first novel (attached). I expect the designs to use copyright free images/visuals, I will not pay for additional stock footage
Updates

Thanks to those who have already submitted initial designs. I have attached example visuals of Protest Art from Japan in the 1950s. I wish to make it explicitly clear that I do not own the copyright for these visuals and so they cannot be used. They are there only as reference material. All of the designs so far have used these visuals 'as is' Secondly there is an unexplained murder in the plot, a man is found drowned in suspicious circumstances, hence why one of the protest art visuals is a drowning man. Thirdly the spy is a Japanese women, a communist sympathiser turned provocateur. She is in her early 30s and is an art enthusiast. She is recruited by Russian intelligence at a protest art exhibition Fourthly please remember this is an e-book. Thumbnails are small on Brindlemart so the thumbnail visual must stand out clearly. You should use that as a 'test' before submitting ideas.

Target Market(s)

readers of historical fiction, spy stories. People who are interested in the cold war and Korea-Japan

Requirements
Must have
• This novel is historical fiction and a lot of time has been spent researching archives in English and Japanese for authenticity. There are references to protest art in the plot. Some actual examples attached below. The front cover should look like these in style, however I cannot use these exact images. My spy is a Japanese women, in her 30s, single, interested in art and literature. The front cover visual must have stand out impact when it appears as a thumbnail on Brindlemart
Nice to have
• (FYI Sakaiminato - photo attached) is where the weapons testing takes place. Not necessary to be on the cover, but to give you an idea of the area. It is remote Japan over 800KM from Tokyo
Should not have
• any stock footage/images that require additional costs

```html
<!DOCTYPE html>
<html lang="en">
<head>
<meta charset="utf-8">
<title>The Copper Lantern — Cover Spread</title>
<link rel="stylesheet" href="https://fonts.googleapis.com/css2?family=Poppins:wght@300;400;600&family=Montserrat:wght@600;700&display=swap">
<style>
  :root {
    --backdrop: #d9d9d9;
    --paper: #f4f4f2;
    --paper-shade: #ebebe8;
    --ink: #1c1c1c;
    --ink-soft: #4a4a4a;
    --sun-red: #c8203a;
    --title-on-sun: #ffffff;
    --sketch-green: #c9cfa8;
    --sketch-green-deep: #9aa273;
    --blossom-grey: #d7d5d2;
  }
  * { box-sizing: border-box; margin: 0; padding: 0; }
  html, body {
    width: 1200px; height: 900px; overflow: hidden;
    background: var(--backdrop);
  }
  .cover-spread {
    position: absolute; left: 70px; top: 75px;
    width: 1060px; height: 750px;
    display: flex;
    box-shadow: 0 18px 40px rgba(0,0,0,0.18);
  }

  /* Back cover */
  .back-cover {
    position: relative; width: 500px; height: 750px;
    background: var(--paper);
    display: flex; flex-direction: column; align-items: center;
    padding-top: 104px;
  }
  .back-title {
    position: relative; z-index: 1;
    font-family: "Montserrat", sans-serif; font-weight: 700;
    font-size: 26px; letter-spacing: 5px; color: var(--ink);
    text-transform: uppercase; white-space: nowrap;
  }
  .blurb {
    position: relative; z-index: 1;
    width: 360px; text-align: center;
    font-family: "Poppins", sans-serif; font-weight: 300;
    font-size: 14px; line-height: 2.05; letter-spacing: 1.8px;
    color: var(--ink-soft);
  }
  .blurb-first { margin-top: 34px; }
  .blurb-second { margin-top: 48px; }
  .blossom-sprig {
    position: absolute; border-radius: 50%;
    background: radial-gradient(circle, var(--blossom-grey) 0%, rgba(215,213,210,0) 72%);
  }
  .blossom-sprig.top { left: 28px; top: 22px; width: 72px; height: 72px; }
  .blossom-sprig.bottom { right: 34px; bottom: 28px; width: 84px; height: 90px; }

  /* Spine */
  .spine {
    position: relative; width: 60px; height: 750px;
    background: var(--paper-shade);
    border-left: 1px solid #deded9; border-right: 1px solid #deded9;
  }
  .spine-text {
    position: absolute; left: 50%; top: 0;
    width: 750px; height: 60px;
    transform-origin: 0 0;
    transform: translateX(30px) rotate(90deg);
    display: flex; align-items: center; justify-content: space-between;
    padding: 0 60px 0 48px;
  }
  .spine-title {
    font-family: "Montserrat", sans-serif; font-weight: 600;
    font-size: 22px; letter-spacing: 7px; color: var(--ink);
  }
  .spine-author {
    font-family: "Montserrat", sans-serif; font-weight: 700;
    font-size: 13px; letter-spacing: 3px; color: var(--ink);
  }

  /* Front cover */
  .front-cover {
    position: relative; width: 500px; height: 750px;
    background: var(--paper); overflow: hidden;
  }
  .front-art { position: absolute; inset: 0; }
  .subtitle {
    position: absolute; left: 34px; top: 34px; width: 300px;
    font-family: "Poppins", sans-serif; font-weight: 400;
    font-size: 11.5px; line-height: 1.3; letter-spacing: 1.6px;
    color: var(--ink-soft); text-transform: uppercase;
  }
  .front-author {
    position: absolute; left: 0; right: 0; bottom: 78px; text-align: center;
    font-family: "Montserrat", sans-serif; font-weight: 700;
    font-size: 30px; letter-spacing: 4px; color: var(--ink);
  }
</style>
</head>
<body>
  <main class="cover-spread">
    <section class="back-cover">
      <div class="blossom-sprig top" role="img" aria-label="Small ink drawing of a cherry blossom sprig"></div>
      <h2 class="back-title">The Copper Lantern</h2>
      <p class="blurb blurb-first">The Korean war has exploded. Neighbouring Japan is the staging post for US troops. Moscow encourages sabotage with its newly expanded spy network. There is a scramble to develop new weapons. Tungsten, a key component for shells, is scarce.</p>
      <p class="blurb blurb-second">A communist sympathiser turned provocateur uncovers a secret weapons testing facility. The leaked news petrifies Washington and Tokyo. A talented counter intelligence officer is charged with tracking down the Soviet intelligence network. Is it too late?</p>
      <div class="blossom-sprig bottom" role="img" aria-label="Small ink drawing of a cherry blossom sprig"></div>
    </section>

    <section class="spine">
      <div class="spine-text">
        <span class="spine-title">THE COPPER LANTERN</span>
        <span class="spine-author">REIKO MATSUDAIRA</span>
      </div>
    </section>

    <section class="front-cover">
      <svg class="front-art" width="500" height="750" viewBox="0 0 500 750">
        <defs>
          <radialGradient id="sketch-wash" cx="0.45" cy="0.45" r="0.6">
            <stop offset="0" stop-color="#9aa273" stop-opacity="0.55"/>
            <stop offset="0.6" stop-color="#c9cfa8" stop-opacity="0.45"/>
            <stop offset="1" stop-color="#c9cfa8" stop-opacity="0"/>
          </radialGradient>
          <linearGradient id="blossom-wash" x1="0" y1="0" x2="0.3" y2="1">
            <stop offset="0" stop-color="#d7d5d2" stop-opacity="0.25"/>
            <stop offset="0.6" stop-color="#d7d5d2" stop-opacity="0.9"/>
            <stop offset="1" stop-color="#c9c4bf" stop-opacity="0.9"/>
          </linearGradient>
        </defs>
        <rect class="sketch-portrait" x="0" y="60" width="340" height="300" fill="url(#sketch-wash)"
              role="img" aria-label="Soft green pencil sketch of a woman's portrait in the style of 1950s protest art"/>
        <path class="blossom-branch" d="M300 230 Q420 200 500 260 L500 750 L330 750 Q360 600 300 520 Q260 420 300 230 Z"
              fill="url(#blossom-wash)" role="img" aria-label="Ink drawing of a flowering cherry blossom branch"/>
        <circle class="rising-sun" cx="265" cy="350" r="165" fill="#c8203a" fill-opacity="0.92"/>
        <text class="front-title" x="265" y="358" text-anchor="middle" font-family="Montserrat, sans-serif" font-weight="600"
              font-size="21" letter-spacing="2.5" fill="#ffffff">THE COPPER LANTERN</text>
      </svg>
      <p class="subtitle">A female spy uncovers secret weapons testing in cold-war Japan</p>
      <h1 class="front-author">REIKO MATSUDAIRA</h1>
    </section>
  </main>
</body>
</html>
```